Brindlewisp Stones

We are making a lable for a jar or a cellophane package for CBD&CBG gummies.

My Idea is an astronaut on the moon with a Hollywood billboard with the brand name. Put a goldchain on the person with a Hemp Leaf medallion. Thats my only Idea but I need to see yours.

Target Market(s)

Every adult over 21

Requirements
Must have
• I included 2 methods to package gummies (2 example of other's product). An idea only, the gummies could be astronauts instead of bears.

```html
<!DOCTYPE html>
<html lang="en">
<head>
<meta charset="UTF-8">
<title>Brindlewisp Stones – Gummy Astronauts</title>
<link href="https://fonts.googleapis.com/css2?family=Oswald:wght@500;600;700&display=swap" rel="stylesheet">
<style>
  :root{
    --ink:#111111;
    --green:#2fb24c;
    --white:#ffffff;
    --paper:#ffffff;
    --pouch-light:#f4f4f5;
    --pouch-purple:#5b2c87;
    --moon-light:#e3e3e6;
    --moon-mid:#c9c9ce;
    --suit:#b9b9bd;
    --suit-dark:#4a4a4d;
  }
  *{box-sizing:border-box;margin:0;padding:0}
  html,body{width:1200px;height:1200px;overflow:hidden;background:var(--paper)}
  body{position:relative;font-family:"Oswald",sans-serif}

  /* Brand lockup */
  .brand-lockup{position:absolute;left:238px;top:100px;width:570px}
  .brand-name{font-weight:700;color:var(--ink);text-transform:uppercase;line-height:1;white-space:nowrap}
  .brand-name .line1{display:block;font-size:100px;letter-spacing:-2px}
  .brand-name .line2{display:block;font-size:92px;letter-spacing:42px;margin-top:4px}
  .mascot{position:absolute;left:830px;top:40px;width:165px;height:330px;border-radius:70px 70px 30px 30px;
    background:linear-gradient(180deg,var(--suit-dark) 0%,var(--suit) 25%,var(--suit) 80%,var(--suit-dark) 100%)}

  /* Pouches */
  .pouch{position:absolute;top:405px;height:770px;border-radius:14px;overflow:hidden}
  .pouch--white{left:100px;width:445px;background:var(--pouch-light);border:1px solid #dedee2}
  .pouch--purple{left:640px;width:465px;background:var(--pouch-purple)}
  .pouch .seal{position:absolute;left:0;right:0;top:55px;height:4px;background:rgba(0,0,0,.08)}
  .pouch .moon{position:absolute;left:40px;top:235px;width:390px;height:390px;border-radius:50%;
    background:radial-gradient(circle at 40% 40%,var(--moon-light),var(--moon-mid))}
  .pouch--purple .moon{left:50px;opacity:.75}
  .tagline{position:absolute;left:0;right:0;top:160px;text-align:center;color:var(--green);
    font-weight:600;font-size:30px;letter-spacing:.5px}
  .pouch-name{position:absolute;left:0;right:0;top:210px;text-align:center;font-weight:700;
    text-transform:uppercase;line-height:.95;color:var(--ink);z-index:2;white-space:nowrap}
  .pouch--purple .pouch-name{color:var(--white)}
  .pouch-name .line1{display:block;font-size:66px;letter-spacing:-.5px}
  .pouch-name .line2{display:block;font-size:60px;letter-spacing:5px}
  .product-title{position:absolute;left:70px;top:405px;width:190px;color:var(--green);font-weight:600;
    font-size:37px;line-height:1.12;letter-spacing:-.5px;text-align:center;z-index:3;white-space:nowrap}
  .pouch--purple .product-title{color:var(--white);left:95px}
  .gummies{position:absolute;left:75px;top:520px;width:150px;height:100px;border-radius:40px;z-index:2;
    background:linear-gradient(90deg,#b36a2d,#c23a2a,#6a2a8a,#2a4fb3,#2f9a3a,#c9b52a)}
  .pouch--purple .gummies{left:95px}
  .astronaut{position:absolute;left:285px;top:370px;width:140px;height:255px;z-index:2;border-radius:60px 60px 24px 24px;
    background:linear-gradient(180deg,var(--suit-dark) 0%,var(--suit) 25%,var(--suit) 80%,var(--suit-dark) 100%)}
  .pouch--purple .astronaut{left:300px}
  .dose-band{position:absolute;left:0;right:0;top:630px;height:58px;background:var(--green);z-index:3;
    color:var(--white)}
  .dose-band .dose{position:absolute;left:85px;top:8px;font-size:36px;font-weight:600;letter-spacing:.5px;line-height:1.1}
  .dose-band .dose-note{position:absolute;left:272px;top:12px;font-size:17px;font-weight:600;line-height:1;white-space:nowrap}
  .dose-band .dose-note small{display:block;font-size:10px;font-weight:500;margin-top:2px}
  .pouch--purple .dose-band .dose{left:90px}
  .pouch--purple .dose-band .dose-note{left:272px}
  .legal{position:absolute;left:0;right:0;top:705px;text-align:center;color:var(--ink);z-index:2}
  .pouch--purple .legal{color:var(--white)}
  .legal .supplement{display:block;font-size:10px;font-weight:500}
  .legal .weight{display:block;font-size:17px;font-weight:600}
</style>
</head>
<body>
  <header class="brand-lockup">
    <h1 class="brand-name"><span class="line1">Brindlewisp</span><span class="line2">Stones</span></h1>
  </header>
  <div class="mascot" role="img" aria-label="Illustration of an astronaut mascot wearing a gold chain with a medallion"></div>

  <section class="pouch pouch--white">
    <div class="seal"></div>
    <div class="moon" role="img" aria-label="Soft grey full moon backdrop"></div>
    <p class="tagline">PREMIUM CDB EDIBLES</p>
    <h2 class="pouch-name"><span class="line1">Brindlewisp</span><span class="line2">Stones</span></h2>
    <p class="product-title">GUMMY<br>ASTRONAUTS</p>
    <div class="gummies" role="img" aria-label="Pile of colourful astronaut-shaped gummies"></div>
    <div class="astronaut" role="img" aria-label="Illustration of the astronaut mascot with gold chain"></div>
    <div class="dose-band">
      <span class="dose">CBD 75MG</span>
      <span class="dose-note">APPROX. PER POUCH<small>(approx. 5.5mg per gummy)</small></span>
    </div>
    <p class="legal"><span class="supplement">DIETARY SUPPLEMENT</span><span class="weight">NET WT 40G</span></p>
  </section>

  <section class="pouch pouch--purple">
    <div class="seal"></div>
    <div class="moon" role="img" aria-label="Soft grey full moon backdrop"></div>
    <p class="tagline">PREMIUM CDB EDIBLES</p>
    <h2 class="pouch-name"><span class="line1">Brindlewisp</span><span class="line2">Stones</span></h2>
    <p class="product-title">GUMMY<br>ASTRONAUTS</p>
    <div class="gummies" role="img" aria-label="Pile of colourful astronaut-shaped gummies"></div>
    <div class="astronaut" role="img" aria-label="Illustration of the astronaut mascot with gold chain"></div>
    <div class="dose-band">
      <span class="dose">CBD 75MG</span>
      <span class="dose-note">APPROX. PER POUCH<small>(approx. 5.5mg per gummy)</small></span>
    </div>
    <p class="legal"><span class="supplement">DIETARY SUPPLEMENT</span><span class="weight">NET WT 40G</span></p>
  </section>
</body>
</html>
```